Project management consultancy needs a website designed

Our company (Keystone PMO) currently has a website (http://www.keystonepmo-example.com.au) that needs to be re-designed and enhanced. Company is a professional services/consultancy business focused on project management. We are looking for something more professional. It would be advantageous if the website can be hosted in SharePoint. We are reasonably happy with the content, what we're after is something that has better aesthetics. Attached to the brief is a copy of our logo in vector format.

Target Market(s)

Small to medium businesses

Industry/Entity Type

It Company

Contact Information for Business Card

logo/company name on back, contact details plus smaller logo on front. Information to display = Name, title, address, phone number, email address, website address

Coding

Coded - Design and coding required

Number of Pages Required

4 page

Font styles to use
Sans Serif

Requirements
Must have
• Website must have: A home page, content page, contact details page (including a contact us function), blog. Project management related images/photos
Nice to have
• Website has the ability to support video content

```html
<!DOCTYPE html>
<html lang="en">
<head>
<meta charset="utf-8">
<title>Keystone PMO</title>
<link rel="stylesheet" href="https://fonts.googleapis.com/css2?family=Montserrat:wght@700&family=Open+Sans:ital,wght@0,400;0,600;1,400&family=Questrial&display=swap">
<style>
:root{
  --blue:#1f5fc7;
  --blue-dark:#1749a8;
  --blue-bright:#2a72e0;
  --text:#3a3a3a;
  --muted:#666;
  --grey-band:#ebebeb;
  --line:#d6d6d6;
  --white:#fff;
}
*{box-sizing:border-box;margin:0;padding:0}
html,body{width:687px;height:1200px;overflow:hidden;background:var(--white)}
body{position:relative;font-family:"Open Sans",Arial,sans-serif;color:var(--text)}
.abs{position:absolute}
.topnav{left:0;top:0;width:687px;height:28px;background:linear-gradient(var(--blue-bright),var(--blue-dark));display:flex;align-items:center;padding-left:56px;gap:0}
.topnav a,.footnav a{font-family:"Questrial",Arial,sans-serif;font-size:8.6px;text-decoration:none;white-space:nowrap}
.topnav a{color:var(--white);margin-right:20px}
.brand{left:56px;top:39px;display:flex;align-items:center;gap:6px}
.brand-mark{width:31px;height:31px;background:var(--blue);border-radius:4px}
.brand-name{font-family:"Open Sans",Arial,sans-serif;font-weight:600;font-size:16px;color:var(--blue);letter-spacing:-.2px}
.social{top:42px;display:flex;gap:6px;left:550px}
.social span{width:24px;height:24px;border-radius:50%;background:var(--blue-dark)}
.hero{left:0;top:83px;width:687px;height:260px;background:linear-gradient(90deg,#20304a 0%,#2f4a72 35%,#5a7aa0 65%,#8aa3c0 100%)}
.hero-title{left:56px;top:158px;font-family:"Questrial",Arial,sans-serif;font-size:21px;line-height:25px;color:var(--white)}
.hero-text{left:58px;top:216px;width:200px;font-size:6.8px;line-height:8px;color:#dfe6f0}
.btn{background:linear-gradient(var(--blue-bright),var(--blue-dark));color:var(--white);font-family:"Questrial",Arial,sans-serif;font-size:8.5px;display:flex;align-items:center;justify-content:center;border-radius:2px}
.hero-btn{left:56px;top:251px;width:62px;height:26px}
.dots{left:56px;top:292px;display:flex;gap:6px}
.dots i{width:6px;height:6px;border-radius:50%;background:#c8ced8}
.dots i:first-child{background:var(--blue-bright)}
.title{left:0;top:359px;width:687px;text-align:center;font-family:"Montserrat",Arial,sans-serif;font-size:22.5px;color:var(--blue);letter-spacing:.2px}
.subtitle{left:0;top:390px;width:687px;text-align:center;font-style:italic;font-size:8.3px;color:#333}
.video{left:57px;top:423px;width:247px;height:189px;background:linear-gradient(135deg,#4a4d52,#8c9096 50%,#3c3f44)}
.video-bar{left:57px;top:586px;width:247px;height:26px;background:#111}
.intro{left:316px;top:421px;width:314px;font-size:6.7px;line-height:11.8px;color:#333}
.intro p+p{margin-top:20px}
.intro-btn{left:315px;top:566px;width:69px;height:27px}
.provide-band{left:0;top:634px;width:687px;height:219px;background:var(--grey-band)}
.section-head{font-family:"Questrial",Arial,sans-serif;font-size:17px;color:var(--blue)}
.provide-head{left:57px;top:654px}
.card{top:690px;width:182px;height:136px;box-shadow:0 10px 10px -6px rgba(0,0,0,.25)}
.card-photo{height:102px;background:linear-gradient(160deg,#c9d3df,#7b8593 60%,#3a4250)}
.card-label{height:34px;background:linear-gradient(var(--blue-bright),var(--blue-dark));color:var(--white);font-family:"Questrial",Arial,sans-serif;font-size:15px;display:flex;align-items:center;padding-left:10px}
.allow-head{left:57px;top:903px;font-size:14.5px}
.benefits{left:57px;top:938px;width:315px;list-style:none;font-size:7.3px;line-height:12px;color:#333}
.benefits li{position:relative;padding-left:15px;margin-bottom:10px}
.benefits svg{position:absolute;left:0;top:3px}
.tagline{left:57px;top:1058px;font-size:11.8px;color:var(--blue)}
.contact{left:384px;top:908px;width:247px;height:208px;border:1px solid var(--line);background:#fafafa;padding:12px 14px}
.contact h2{font-family:"Questrial",Arial,sans-serif;font-weight:400;font-size:15px;color:var(--blue);margin-bottom:11px}
.field{background:var(--white);border:1px solid var(--line);font-size:7.5px;color:#777;padding:0 8px;display:flex;align-items:center;margin-bottom:5px;height:27px}
.field.msg{height:56px;align-items:flex-start;padding-top:8px}
.submit{width:48px;height:26px;margin-top:9px}
.footer{left:0;top:1144px;width:687px;height:56px;background:linear-gradient(#fff,#ececec);border-top:1px solid #e3e3e3}
.footnav{left:57px;top:1160px;display:flex}
.footnav a{color:#555;margin-right:20px}
.copy{left:0;top:1180px;width:687px;text-align:center;font-size:6.3px;color:#555}
</style>
</head>
<body>
<nav class="abs topnav">
  <a href="#">HOME</a><a href="#">WHAT IS A PMO</a><a href="#">HOW DOES A PMO ADD VALUE</a><a href="#">WHAT'S THE ADVANTAGE</a><a href="#">WHY KEYSTONE PMO</a><a href="#">CONTACT US</a><a href="#">BLOG</a>
</nav>

<div class="abs brand"><span class="brand-mark"></span><span class="brand-name">KEYSTONE PMO</span></div>
<div class="abs social" aria-label="Social links"><span></span><span></span><span></span></div>

<div class="abs hero" role="img" aria-label="Smiling businessman in glasses and a suit"></div>
<h1 class="abs hero-title">Project<br>Management</h1>
<p class="abs hero-text">Neque porro quisquam est, qui dolorem ipsum quia dolor sit amet, consectetur,</p>
<a class="abs btn hero-btn">Read More</a>
<div class="abs dots"><i></i><i></i><i></i></div>

<h2 class="abs title">KEYSTONE PORTFOLIO MANAGEMENT OFFICE</h2>
<p class="abs subtitle">Offering you a competitive alternative to traditional in-house PMOs</p>

<div class="abs video" role="img" aria-label="Video still of hands reviewing charts on paperwork"></div>
<svg class="abs" style="left:164px;top:489px" width="34" height="34" viewBox="0 0 34 34"><circle cx="17" cy="17" r="15.5" fill="none" stroke="#fff" stroke-width="2"/><path d="M13 10 L24 17 L13 24Z" fill="#fff"/></svg>
<svg class="abs video-bar" width="247" height="26" viewBox="0 0 247 26">
  <rect width="247" height="26" fill="#111"/>
  <circle cx="17" cy="13" r="6" fill="#444"/><path d="M15 10 L20 13 L15 16Z" fill="#ccc"/>
  <rect x="30" y="12" width="80" height="2" fill="#444"/><circle cx="33" cy="13" r="3" fill="#fff"/>
  <text x="101" y="16" font-size="7" fill="#fff" font-family="Arial,sans-serif">00:00 /</text>
  <text x="129" y="16" font-size="7" fill="#e02020" font-family="Arial,sans-serif">00:00</text>
  <path d="M167 11 h3 l3 -3 v10 l-3 -3 h-3z" fill="#bbb"/>
  <circle cx="196" cy="13" r="3" fill="#fff"/>
  <rect x="217" y="9" width="8" height="8" fill="none" stroke="#aaa"/><rect x="229" y="9" width="8" height="8" fill="#555"/>
</svg>
<div class="abs intro">
  <p>Our team of professionals comes equipped with a wealth of experience in both the private and public sectors. Let our professionally certified experts monitor and improve your project management so that you can focus on your business.<br>We aim to align the selection and execution of projects and programs with your organization's business goals, thereby increasing the success of project execution. We provide coordination, guidance, and training to your project teams, coaching them in your company's methodologies and standards for each project.</p>
  <p>Most importantly, we work with you to implement these strategies in a way that works with your individual organization and fits your specific needs.</p>
</div>
<a class="abs btn intro-btn">Read More</a>

<div class="abs provide-band"></div>
<h2 class="abs section-head provide-head">WE PROVIDE</h2>
<div class="abs card" style="left:57px"><div class="card-photo" role="img" aria-label="Team of colleagues in a meeting"></div><div class="card-label">COORDINATION</div></div>
<div class="abs card" style="left:253px"><div class="card-photo" role="img" aria-label="Consultant guiding colleagues at a laptop"></div><div class="card-label">GUIDANCE</div></div>
<div class="abs card" style="left:449px"><div class="card-photo" role="img" aria-label="Group training session at a flipchart"></div><div class="card-label">TRAINING</div></div>

<h2 class="abs section-head allow-head">KEYSTONE PMO WILL ALLOW YOU TO</h2>
<ul class="abs benefits">
  <li><svg width="7" height="7" viewBox="0 0 7 7"><circle cx="3.5" cy="3.5" r="3.5" fill="#333"/><path d="M2.5 1.8 L4.5 3.5 L2.5 5.2" stroke="#fff" fill="none"/></svg>Optimize the use of your capital. We'll help you avoid project inefficiency and maximize success by choosing the right projects the first time, every time.</li>
  <li><svg width="7" height="7" viewBox="0 0 7 7"><circle cx="3.5" cy="3.5" r="3.5" fill="#333"/><path d="M2.5 1.8 L4.5 3.5 L2.5 5.2" stroke="#fff" fill="none"/></svg>Filter out the noise; you have enough on your plate without being inundated with data. We'll communicate efficiently to provide you with the important information you need.</li>
  <li><svg width="7" height="7" viewBox="0 0 7 7"><circle cx="3.5" cy="3.5" r="3.5" fill="#333"/><path d="M2.5 1.8 L4.5 3.5 L2.5 5.2" stroke="#fff" fill="none"/></svg>Let Project Managers focus on what they know best-- project outcomes. They won't have be burdened with administration.</li>
</ul>
<p class="abs tagline">You know your business, we know PMOs.</p>

<form class="abs contact">
  <h2>QUICK CONTACT</h2>
  <div class="field">Name</div>
  <div class="field">Email</div>
  <div class="field msg">Message</div>
  <div class="btn submit">Submit</div>
</form>

<footer class="abs footer"></footer>
<nav class="abs footnav">
  <a href="#">HOME</a><a href="#">WHAT IS A PMO</a><a href="#">HOW DOES A PMO ADD VALUE</a><a href="#">WHAT'S THE ADVANTAGE</a><a href="#">WHY KEYSTONE PMO</a><a href="#">CONTACT US</a><a href="#">BLOG</a>
</nav>
<p class="abs copy">©2015keystonepmo-example.com.au. All rights reserved.</p>
</body>
</html>
```